Letterhead for a Natural Hair Run

We need a letterhead design with the logo uploaded entitled 'Coralwave 5K'. This run is a natural 5K run seeking to promote the acceptance of natural beauty in every aspect of society encompassing one's ethnic roots and its connection to a healthy lifetstyle. We would like to see designs coordinating with our logo. The design should be fun and exciting!

Industry/Entity Type

Hair

Font styles to use
Serif
Sans Serif

Requirements
Must have
• Please included this information on the letter head:
• P.O. Box K7214
• Kestrel Bay, Solmara
• Phone: (242) 618-2097
• Email: goskyward517@mailbrisk.net

```html
<!DOCTYPE html>
<html lang="en">
<head>
<meta charset="utf-8">
<title>Coralwave 5K Letterhead</title>
<link rel="stylesheet" href="https://fonts.googleapis.com/css2?family=Arimo:wght@400&display=swap">
<style>
  :root {
    --paper: #ffffff;
    --ink: #1b1b1b;
    --sun: #f4e35a;
    --sea: #3bbad4;
    --contact-text: #f4e35a;
    --icon: #ffffff;
  }
  html, body {
    margin: 0;
    padding: 0;
    width: 992px;
    height: 1200px;
    overflow: hidden;
    background: var(--paper);
  }
  .letterhead {
    position: relative;
    width: 992px;
    height: 1200px;
    background: var(--paper);
    font-family: "Arimo", Arial, sans-serif;
  }
  .brand {
    position: absolute;
    left: 70px;
    top: 80px;
    display: flex;
    align-items: center;
    gap: 12px;
  }
  .brand-dot {
    width: 22px;
    height: 22px;
    border-radius: 50%;
    background: var(--sea);
  }
  .brand-name {
    font-size: 30px;
    font-weight: 400;
    color: var(--ink);
    letter-spacing: 1px;
    white-space: nowrap;
  }
  .footer-wave {
    position: absolute;
    left: 0;
    top: 0;
    width: 992px;
    height: 1200px;
  }
  .contact {
    position: absolute;
    left: 665px;
    top: 1020px;
    list-style: none;
    margin: 0;
    padding: 0;
    color: var(--contact-text);
    font-size: 17px;
    line-height: 30px;
    white-space: nowrap;
  }
  .contact li {
    display: flex;
    align-items: center;
    gap: 14px;
  }
  .contact svg {
    width: 18px;
    height: 18px;
    flex: none;
  }
</style>
</head>
<body>
<div class="letterhead">
  <div class="brand">
    <span class="brand-dot"></span>
    <span class="brand-name">Coralwave 5K</span>
  </div>

  <svg class="footer-wave" viewBox="0 0 992 1200" aria-hidden="true">
    <path fill="var(--sun)" d="M330,1200 C370,1080 470,1000 610,990 L700,985 C760,960 800,800 870,720 C920,665 960,650 992,640 L992,1200 Z"/>
    <path fill="var(--sea)" d="M354,1200 C394,1095 492,1018 625,1010 L712,1005 C778,978 818,822 888,744 C932,694 966,680 992,672 L992,1200 Z"/>
  </svg>

  <ul class="contact">
    <li>
      <svg viewBox="0 0 20 20"><path fill="var(--icon)" d="M4 5h12v11H4z M4 5l6-3 6 3"/></svg>
      <span>P.O. Box K7214</span>
    </li>
    <li>
      <svg viewBox="0 0 20 20"><path fill="var(--icon)" d="M10 2l8 7h-2v8h-4v-5H8v5H4V9H2z"/></svg>
      <span>Kestrel Bay, Solmara</span>
    </li>
    <li>
      <svg viewBox="0 0 20 20"><path fill="var(--icon)" d="M5 2l3 4-2 2c1 2 4 5 6 6l2-2 4 3-2 3C9 18 2 11 2 4z"/></svg>
      <span>Phone: (242) 618-2097</span>
    </li>
    <li>
      <svg viewBox="0 0 20 20"><path fill="var(--icon)" d="M2 5h16v11H2z"/><path fill="none" stroke="var(--sea)" stroke-width="1.5" d="M2 5l8 6 8-6"/></svg>
      <span>Email: goskyward517@mailbrisk.net</span>
    </li>
  </ul>
</div>
</body>
</html>
```